Commercial and Residential landscape Flyer design

we would like a flyer to advertise our new landscaping division for our company. Phone Number 5184620371
email pinecrestgroundworkservices@mailorbit.net
address 7 Marlow Court Schenectady New York 12419
The design is up to you. ill attach some sample flyers in the file section
Target Market(s)
Residential and commercial properties
Industry/Entity Type
Landscape
Font styles to use
Sans Serif
Colors
Designer to choose colors to be used in the design.
Requirements
Must have
- Services offered
- Spring Cleanups
- Mulch installation
- Mowing
- Tree and shrub Maintenance
- Fall Cleanups
- Fully Insured
- Free Estimates
Nice to have
- See word file Please double check all grammar and spelling
- Feel free to use anything in the word file. Its totally up to you. It all doesn't need to be on it . would like to stick with the color scheme of the logo
Should not have
- there are no should not haves. We just want to get the word out that we have a landscape division

```html
<!DOCTYPE html>
<html lang="en">
<head>
<meta charset="utf-8">
<title>Commercial and Residential Landscaping Flyer</title>
<link rel="stylesheet" href="https://fonts.googleapis.com/css2?family=Montserrat:wght@600;700;800&family=Nunito+Sans:wght@400;600;700&display=swap">
<style>
  :root {
    --blue: #1a86e4;
    --blue-dark: #0f6fc6;
    --ink: #131313;
    --grey-text: #3a3a3a;
    --heading-grey: #4a4a4a;
    --white: #ffffff;
    --stage: #e6e6e6;
    --head-font: "Montserrat", sans-serif;
    --body-font: "Nunito Sans", sans-serif;
  }
  * { box-sizing: border-box; margin: 0; padding: 0; }
  html, body { width: 1200px; height: 902px; overflow: hidden; }
  body { background: var(--stage); position: relative; font-family: var(--body-font); color: var(--grey-text); }

  .flyer { position: absolute; top: 50px; width: 568px; height: 803px; background: var(--white); overflow: hidden; box-shadow: 0 3px 10px rgba(0,0,0,.25); }
  .flyer--front { left: 21px; }
  .flyer--back { left: 607px; }
  .abs { position: absolute; }

  /* ---------- front ---------- */
  .front-header { left: 0; top: 0; width: 568px; height: 82px; background: var(--ink); text-align: center; font-family: var(--head-font); font-weight: 800; font-size: 25px; line-height: 29px; padding-top: 13px; color: var(--white); letter-spacing: .3px; }
  .front-header .accent { color: var(--blue); display: block; }
  .hero-photo { left: 0; top: 82px; width: 568px; height: 226px; background: linear-gradient(180deg, #8fb8d8 0%, #a9c98d 30%, #6f8f4a 55%, #d46aa8 72%, #4f8a34 100%); }
  .insured-seal { left: 16px; top: 110px; width: 122px; height: 122px; border-radius: 50%; background: var(--white); border: 4px solid var(--blue); }
  .blue-band { left: 0; top: 306px; width: 568px; height: 104px; background: var(--blue); }
  .brand-dome { left: 180px; top: 312px; width: 210px; height: 130px; background: var(--white); border-radius: 105px 105px 0 0; }
  .brand-name { left: 180px; top: 374px; width: 210px; text-align: center; font-family: var(--head-font); font-weight: 800; font-size: 14px; line-height: 17px; color: var(--blue); }
  .circle-photo { border-radius: 50%; border: 6px solid var(--blue); }
  .circle-photo--planting { left: 17px; top: 267px; width: 148px; height: 148px; background: radial-gradient(circle at 45% 40%, #7fae56 0%, #6a4a2e 70%, #4a3320 100%); }
  .circle-photo--mowing { left: 401px; top: 267px; width: 148px; height: 148px; background: radial-gradient(circle at 50% 60%, #2fb34a 0%, #4d8a3a 55%, #2d5a28 100%); }

  .pill { background: var(--blue); color: var(--white); font-family: var(--head-font); font-weight: 700; text-align: center; border-radius: 16px; white-space: nowrap; }
  .pill--beautify { left: 157px; top: 450px; width: 254px; height: 28px; font-size: 14px; line-height: 28px; }
  .pill--design { left: 99px; top: 617px; width: 369px; height: 28px; font-size: 14px; line-height: 28px; }
  .body-copy { font-size: 10.2px; line-height: 12.6px; text-align: center; color: var(--grey-text); }
  .body-copy--beautify { left: 17px; top: 487px; width: 534px; }
  .body-copy--design { left: 28px; top: 654px; width: 512px; }

  .call-box { left: 16px; top: 722px; width: 253px; height: 65px; border: 2px dashed #666; border-radius: 12px; font-family: var(--head-font); font-weight: 800; font-size: 17.5px; line-height: 24px; padding: 7px 0 0 13px; color: var(--blue); white-space: nowrap; }
  .call-box .dark { color: #555; }
  .front-footer { left: 260px; top: 720px; width: 308px; height: 83px; }
  .contact-line { display: flex; align-items: center; gap: 7px; font-family: var(--head-font); font-weight: 700; font-size: 9.5px; color: var(--white); white-space: nowrap; }
  .contact-line svg { width: 11px; height: 11px; fill: var(--blue); flex: none; }
  .front-contact--email { left: 312px; top: 754px; }
  .front-contact--address { left: 312px; top: 776px; }

  /* ---------- back ---------- */
  .back-photo { left: 0; top: 0; width: 568px; height: 374px; background: linear-gradient(170deg, #6fa9de 0%, #c9d6e0 30%, #c9b27a 48%, #e7b63a 60%, #5c9a3a 75%, #d74f8e 90%, #3f7d2d 100%); }
  .back-panel { left: 0; top: 226px; width: 330px; height: 148px; }
  .panel-title { left: 19px; top: 240px; font-family: var(--head-font); font-weight: 700; font-size: 15px; color: var(--blue); padding-bottom: 4px; border-bottom: 1.5px solid var(--white); white-space: nowrap; }
  .panel-copy { left: 14px; top: 274px; width: 272px; font-size: 10.2px; line-height: 12.7px; color: var(--white); }
  .circle-photo--patio { left: 397px; top: 26px; width: 154px; height: 154px; background: linear-gradient(180deg, #9fb7c9 0%, #b8a488 45%, #4e9a3b 100%); }
  .circle-photo--path { left: 297px; top: 168px; width: 142px; height: 142px; background: radial-gradient(circle at 50% 55%, #7cc24d 0%, #3e8a2c 60%, #c5447a 100%); }
  .cta-shape { left: 328px; top: 322px; width: 240px; height: 52px; }
  .cta-text { left: 360px; top: 330px; width: 204px; font-family: var(--head-font); font-weight: 800; font-size: 15px; line-height: 19px; color: var(--white); text-align: center; white-space: nowrap; }

  .pill--cleanup { left: 191px; top: 384px; width: 187px; height: 27px; font-size: 14px; line-height: 27px; }
  .body-copy--cleanup { left: 29px; top: 422px; width: 512px; }
  .tick-list { display: flex; justify-content: center; gap: 11px; font-family: var(--head-font); font-weight: 700; font-size: 10.6px; color: var(--ink); }
  .tick-list li { list-style: none; display: flex; align-items: center; gap: 6px; }
  .tick-list svg { width: 10px; height: 10px; flex: none; }
  .tick-list--top { left: 0; top: 470px; width: 568px; }
  .tick-list--bottom { left: 0; top: 485px; width: 568px; }

  .maintain-band { left: 0; top: 518px; width: 568px; height: 42px; background: var(--blue); color: var(--white); font-family: var(--head-font); font-weight: 800; font-size: 18px; line-height: 42px; text-align: center; letter-spacing: .2px; white-space: nowrap; }
  .tree-heading { left: 0; top: 569px; width: 568px; text-align: center; font-family: var(--head-font); font-weight: 700; font-size: 22px; color: var(--heading-grey); }
  .body-copy--trees { left: 17px; top: 604px; width: 534px; }

  .service-panel { left: 0; top: 654px; width: 568px; height: 116px; }
  .pill--services { left: 191px; top: 661px; width: 187px; height: 27px; font-size: 14px; line-height: 27px; background: var(--ink); }
  .service-list { left: 0; top: 704px; width: 568px; font-family: var(--head-font); font-weight: 700; font-size: 10.8px; line-height: 15.2px; color: var(--white); display: flex; flex-direction: column; align-items: center; }
  .service-list li { list-style: none; display: flex; align-items: center; gap: 6px; }
  .service-list svg { width: 10px; height: 10px; flex: none; }
  .back-footer { left: 0; top: 769px; width: 568px; height: 34px; background: var(--ink); display: flex; justify-content: center; align-items: center; gap: 12px; }
</style>
</head>
<body>
<svg width="0" height="0" style="position:absolute">
  <defs>
    <symbol id="icon-tick-blue" viewBox="0 0 12 12"><rect x="1" y="2" width="9" height="9" fill="none" stroke="#1a86e4" stroke-width="1.4"/><path d="M3 6.5 5.3 8.8 11 2" fill="none" stroke="#1a86e4" stroke-width="1.6"/></symbol>
    <symbol id="icon-tick-white" viewBox="0 0 12 12"><rect x="1" y="2" width="9" height="9" fill="none" stroke="#fff" stroke-width="1.4"/><path d="M3 6.5 5.3 8.8 11 2" fill="none" stroke="#fff" stroke-width="1.6"/></symbol>
    <symbol id="icon-mail" viewBox="0 0 12 12"><rect x="0.5" y="2" width="11" height="8" rx="1"/><path d="M1 2.6 6 6.6 11 2.6" fill="none" stroke="#131313" stroke-width="1"/></symbol>
    <symbol id="icon-pin" viewBox="0 0 12 12"><path d="M6 0.5a4 4 0 0 0-4 4c0 3 4 7 4 7s4-4 4-7a4 4 0 0 0-4-4zm0 5.6a1.6 1.6 0 1 1 0-3.2 1.6 1.6 0 0 1 0 3.2z"/></symbol>
  </defs>
</svg>

<!-- front page -->
<section class="flyer flyer--front">
  <header class="abs front-header">COMMERCIAL AND RESIDENTIAL<span class="accent">LANDSCAPING</span></header>
  <div class="abs hero-photo" role="img" aria-label="Two-storey house with a manicured lawn and blooming pink rhododendrons"></div>
  <div class="abs insured-seal" role="img" aria-label="Fully insured seal"></div>
  <div class="abs blue-band"></div>
  <div class="abs circle-photo circle-photo--planting" role="img" aria-label="Gloved hands planting flowers in soil"></div>
  <div class="abs circle-photo circle-photo--mowing" role="img" aria-label="Green ride-on lawn mower cutting grass"></div>
  <div class="abs brand-dome"></div>
  <div class="abs brand-name">PINECREST<br>GROUNDWORK<br>SERVICES</div>

  <div class="abs pill pill--beautify">Beautify Your Yard or Business</div>
  <p class="abs body-copy body-copy--beautify">We can help you with all phases of the landscaping process, from designing an interesting, cohesive lWe can help you with all phases of the landscaping process, from designing an interesting, cohesive layout to installation. In addition to planting trees, shrubs, and flowers, our services also include the design and installation of the following landscaping features: Gardens, including Terraced Gardens, Patios, Walkways, Retaining Walls, and Xeriscaping. In addition, we provide seeding and sodding services, and we can also implement rock and mulch beds. Layout to installation. In addition to planting trees, shrubs, and flowers, our services also include the design and installation of the following landscaping features: Gardens, including Terraced Gardens, Patios, Walkways, Retaining Walls, and Xeriscaping. In addition, we provide seeding and sodding services, and we can also implement rock and mulch beds.</p>

  <div class="abs pill pill--design">Implement a Responsible Landscaping Design</div>
  <p class="abs body-copy body-copy--design">At Pinecrest Groundwork Services, we are passionate about creating landscapes that are sustainable as well as beautiful. That's why we emphasize the use of xeriscape plants, healthy soils, and water-friendly designs in all landscapes we work on. When you rely on us for commercial and residential landscaping services, your business or yard will be healthy and your conscience clear.</p>

  <div class="abs call-box">CALL US 5184620371<br><span class="dark">FOR A </span>FREE ESTIMATE</div>
  <svg class="abs front-footer" viewBox="0 0 308 83" aria-hidden="true">
    <path d="M130 18 C140 8 148 6 160 6 L308 6 L308 83 L130 83 Z" fill="#1a86e4"/>
    <path d="M39 18 L308 18 L308 83 L9 83 Z" fill="#131313"/>
  </svg>
  <div class="abs contact-line front-contact--email"><svg><use href="#icon-mail"/></svg>pinecrestgroundworkservices@mailorbit.net</div>
  <div class="abs contact-line front-contact--address"><svg><use href="#icon-pin"/></svg>7 Marlow Court Schenectady New York 12419</div>
</section>

<!-- back page -->
<section class="flyer flyer--back">
  <div class="abs back-photo" role="img" aria-label="Suburban house with colourful flower beds and a green lawn"></div>
  <svg class="abs back-panel" viewBox="0 0 330 148" aria-hidden="true"><path d="M0 0 L277 0 L325 148 L0 148 Z" fill="#131313"/></svg>
  <div class="abs panel-title">Receive Individualized Services</div>
  <p class="abs panel-copy">We are a family-owned, family-operated business, so we know from experience how important your yard's appearance is to you. We give your yard the same care that we give our own. At the same time, we know that you have your own unique vision for your landscaping, and our design of your yard reflects that. Work with us to create the yard of your dreams.</p>
  <div class="abs circle-photo circle-photo--patio" role="img" aria-label="Backyard patio with fresh lawn and wooden fence"></div>
  <div class="abs circle-photo circle-photo--path" role="img" aria-label="Stepping-stone path through a garden lawn"></div>
  <svg class="abs cta-shape" viewBox="0 0 240 52" aria-hidden="true"><path d="M18 0 L240 0 L240 52 L0 52 Z" fill="#1a86e4"/></svg>
  <div class="abs cta-text">CALL US 5184620371<br>FOR A FREE ESTIMATE</div>

  <div class="abs pill pill--cleanup">Our Cleanup Services</div>
  <p class="abs body-copy body-copy--cleanup">Take comfort in knowing that all our workers are fully insured through workers' compensations. Our lawn cleanup activities include lawn mowing, weed mowing, sucker tree removal, leaf and debris rake up and removal, perennial bed cleanup, and tree and shrub trimming.</p>
  <ul class="abs tick-list tick-list--top">
    <li><svg><use href="#icon-tick-blue"/></svg>Periodic cleanups</li>
    <li><svg><use href="#icon-tick-blue"/></svg>Spring cleanups</li>
    <li><svg><use href="#icon-tick-blue"/></svg>Fall cleanups</li>
  </ul>
  <ul class="abs tick-list tick-list--bottom">
    <li><svg><use href="#icon-tick-blue"/></svg>Special occasion cleanups</li>
    <li><svg><use href="#icon-tick-blue"/></svg>"I just don't have time" cleanups</li>
  </ul>

  <div class="abs maintain-band">MAINTAIN THE TREES &amp; SHRUBS ON YOUR PROPERTY</div>
  <h2 class="abs tree-heading">Tree Trimming, Removal &amp; More</h2>
  <p class="abs body-copy body-copy--trees">If you have trees or shrubs that you need removed from your residential or commercial property then contact Pinecrest Groundwork Services today! Our team will be there in no time to cut those trees down and haul them away for you. We deal in removing small trees (under 20' in height).</p>

  <svg class="abs service-panel" viewBox="0 0 568 116" aria-hidden="true">
    <path d="M0 116 L38 24 C44 10 52 4 70 4 L494 4 C512 4 520 10 526 24 L568 116 Z" fill="#1a86e4"/>
  </svg>
  <div class="abs pill pill--services">Our Cleanup Services</div>
  <ul class="abs service-list">
    <li><svg><use href="#icon-tick-white"/></svg>Tree and shrub removal</li>
    <li><svg><use href="#icon-tick-white"/></svg>Single tree removal</li>
    <li><svg><use href="#icon-tick-white"/></svg>Tree trimming (hazardous limb removal and view cutting)</li>
    <li><svg><use href="#icon-tick-white"/></svg>Installation of new trees, shrubs, perennials, and annuals</li>
  </ul>
  <footer class="abs back-footer">
    <div class="contact-line"><svg><use href="#icon-mail"/></svg>pinecrestgroundworkservices@mailorbit.net</div>
    <div class="contact-line"><svg><use href="#icon-pin"/></svg>7 Marlow Court Schenectady New York 12419</div>
  </footer>
</section>
</body>
</html>
```